Industrial Company-Pop-Up Banner Design for Demolition and Infrastructure Company

Hi-
We need to create 2 pop-up banners for our company. They will both have the same logo, but different photos. We would like to have the colors white, red, and black and feature a modern design. I have attached some inspiration photos.

Target Market(s)

Trade Show/Job Fair Audience

Industry/Entity Type

construction, industrial

Font styles to use
Sans Serif

Colors
EB3D1F
EC4F4E
F09395
F8D3D4
FCEDEE

Requirements
Must have
• 2 versions, each with different photos but same design. Logo, Red, Black, and White Color Scheme, Modern Design
Nice to have
• Modern Design similar to the inspiration photos

```html
<!DOCTYPE html>
<html lang="en">
<head>
<meta charset="utf-8">
<title>R.K. Harlan Companies – Pop-Up Banners</title>
<link href="https://fonts.googleapis.com/css2?family=Fira+Sans:ital,wght@0,600;0,700;1,300&display=swap" rel="stylesheet">
<style>
  :root {
    --page: #ffffff;
    --charcoal: #2b2b2b;
    --charcoal-soft: #363636;
    --red: #e31e26;
    --white: #ffffff;
  }
  html, body {
    margin: 0;
    width: 1200px;
    height: 1000px;
    overflow: hidden;
    background: var(--page);
    font-family: "Fira Sans", Arial, sans-serif;
  }
  .banner {
    position: absolute;
    width: 487px;
    height: 690px;
    box-shadow: 0 4px 10px rgba(0,0,0,0.15);
    overflow: hidden;
  }
  .banner--first { left: 97px; top: 163px; }
  .banner--second { left: 645px; top: 166px; }
  .banner svg { position: absolute; left: 0; top: 0; }
  .tagline {
    position: absolute;
    color: var(--white);
    text-align: center;
    line-height: 1;
    width: 220px;
  }
  .tagline__lead { font-weight: 700; font-size: 17px; letter-spacing: 0.2px; }
  .tagline__accent { font-style: italic; font-weight: 300; font-size: 28px; margin: 5px 0 6px; }
  .tagline__since { font-weight: 700; font-size: 13px; letter-spacing: 0.3px; }
  .banner--first .tagline { left: 7px; top: 282px; }
  .banner--second .tagline { left: 251px; top: 357px; width: 220px; }
  .banner--second .tagline__lead { font-size: 20px; }
  .banner--second .tagline__accent { font-size: 31px; }
  .banner--second .tagline__since { font-size: 15px; }
  .brand {
    position: absolute;
    color: var(--white);
    font-weight: 700;
    text-align: center;
    line-height: 1.15;
  }
  .banner--first .brand { left: 14px; top: 560px; width: 150px; font-size: 16px; }
  .banner--second .brand { left: 276px; top: 266px; width: 180px; font-size: 19px; }
</style>
</head>
<body>

<section class="banner banner--first">
  <svg width="487" height="690" viewBox="0 0 487 690">
    <defs>
      <linearGradient id="plantPhoto" x1="0" y1="0" x2="0" y2="1">
        <stop offset="0" stop-color="#f2f2f2"/>
        <stop offset="0.6" stop-color="#9a9a9a"/>
        <stop offset="1" stop-color="#4a4a4a"/>
      </linearGradient>
      <linearGradient id="sitePhoto" x1="0" y1="0" x2="0" y2="1">
        <stop offset="0" stop-color="#b7c6d6"/>
        <stop offset="0.35" stop-color="#6f6f6f"/>
        <stop offset="1" stop-color="#a8a8a8"/>
      </linearGradient>
    </defs>
    <rect class="photo" role="img" aria-label="Black and white photo of an industrial plant mid-demolition" x="0" y="0" width="487" height="310" fill="url(#plantPhoto)"/>
    <polygon class="band-dark" points="0,174 380,300 487,262 487,690 0,690" fill="var(--charcoal)"/>
    <polygon class="photo" role="img" aria-label="Photo of a haul truck and excavator on an earthworks site" points="55,412 487,262 487,690 305,690" fill="url(#sitePhoto)"/>
    <polygon class="band-red" points="0,442 48,425 285,690 0,690" fill="var(--red)"/>
    <polygon class="wedge-white" points="48,670 487,552 487,562 100,690 48,690" fill="var(--white)"/>
  </svg>
  <div class="tagline">
    <div class="tagline__lead">Building America’s</div>
    <div class="tagline__accent">future</div>
    <div class="tagline__since">SINCE 1962.</div>
  </div>
  <div class="brand">R.K. HARLAN<br>Companies</div>
</section>

<section class="banner banner--second">
  <svg width="487" height="690" viewBox="0 0 487 690">
    <defs>
      <linearGradient id="hangarPhoto" x1="0" y1="0" x2="0" y2="1">
        <stop offset="0" stop-color="#707070"/>
        <stop offset="0.5" stop-color="#c8c8c8"/>
        <stop offset="1" stop-color="#6a6a6a"/>
      </linearGradient>
      <linearGradient id="stationPhoto" x1="0" y1="0" x2="1" y2="1">
        <stop offset="0" stop-color="#9c9c9c"/>
        <stop offset="0.6" stop-color="#6a6a6a"/>
        <stop offset="1" stop-color="#3a3a3a"/>
      </linearGradient>
    </defs>
    <rect class="photo" role="img" aria-label="Black and white photo of an excavator in front of a large assembly building" x="0" y="0" width="487" height="330" fill="url(#hangarPhoto)"/>
    <polygon class="band-dark" points="0,314 487,185 487,690 0,690" fill="var(--charcoal)"/>
    <polygon class="photo" role="img" aria-label="Aerial photo of a power station with conveyor gantries" points="0,380 150,320 460,625 487,690 0,690" fill="url(#stationPhoto)"/>
    <polygon class="band-dark-soft" points="175,300 487,205 487,650" fill="var(--charcoal-soft)"/>
    <polygon class="band-red" points="0,314 70,281 280,524 0,375" fill="var(--red)"/>
  </svg>
  <div class="brand">R.K. HARLAN<br>Companies</div>
  <div class="tagline">
    <div class="tagline__lead">Building America’s</div>
    <div class="tagline__accent">future</div>
    <div class="tagline__since">SINCE 1962.</div>
  </div>
</section>

</body>
</html>
```